Thornwell Building Company - advertisement poster

I am looking to print some canvas signs to advertise my general contracting company, Thornwell Building Company. The sign will measure 6' long x 3' high so the size should match that ratio. I already have a logo icon, which is the Letter 'A' and some trees that I would like to incorporate, see attached. I would also like the to have the following information listed:
1) phone number: 472-318-6095
2) email: thornwellbuildingcompany@mailvistra.net
3) website: thornwellbuildingcompany.com
4) Lic#5386204
5) I want to use this text: "BUILD WITH THE T-CREW!"

The ad should be relatively simple and clean. Black and Green are my company colors. I am open to creative ideas!

Target Market(s)

People looking to renovate their homes

Industry/Entity Type

Construction

Colors
59FF00
82FF00
B8FF75
E3FFCB
F4FFEA

Requirements
Must have
• Must have my company logo
Should not have
• No photos or complex graphics

```html
<!DOCTYPE html>
<html lang="en">
<head>
<meta charset="utf-8">
<title>Thornwell Building Company – Sign</title>
<link rel="stylesheet" href="https://fonts.googleapis.com/css2?family=Bebas+Neue&family=Montserrat:wght@500;600&display=swap">
<style>
  :root {
    --stage: #7a7a7a;
    --black: #000000;
    --green: #72b849;
    --green-dark: #5a9a37;
    --white: #ffffff;
  }
  * { margin: 0; padding: 0; box-sizing: border-box; }
  html, body { width: 1200px; height: 904px; overflow: hidden; background: var(--stage); }
  .sign {
    position: absolute; left: 131px; top: 218px;
    width: 937px; height: 469px;
    background: var(--black); overflow: hidden;
  }
  .sign__shapes { position: absolute; inset: 0; }

  .logo-mark {
    position: absolute; left: 430px; top: 40px;
    width: 78px; height: 78px; background: var(--green);
  }
  .est {
    position: absolute; top: 91px; width: 52px; height: 22px;
    border-top: 1px solid var(--green); border-bottom: 1px solid var(--green);
    color: var(--white); text-align: center;
    font-family: "Montserrat", sans-serif; font-weight: 500;
    font-size: 11px; line-height: 20px; letter-spacing: 2.5px;
  }
  .est--left { left: 315px; }
  .est--right { left: 570px; }

  .brand {
    position: absolute; left: 0; right: 0; top: 136px;
    text-align: center; color: var(--white);
    font-family: "Montserrat", sans-serif; font-weight: 600;
  }
  .brand__name { display: block; font-size: 40px; line-height: 44px; letter-spacing: 2px; }
  .brand__tag { display: block; font-size: 17px; line-height: 22px; letter-spacing: 8px; margin-top: 2px; }

  .headline {
    position: absolute; left: 0; right: 0; top: 222px;
    text-align: center; color: var(--white); white-space: nowrap;
    font-family: "Bebas Neue", sans-serif; font-weight: 400; font-size: 106px;
    line-height: 1; letter-spacing: 1px;
  }
  .contact-band {
    position: absolute; left: 0; top: 342px; width: 100%; height: 108px;
    background: var(--green);
  }
  .phone {
    position: absolute; left: 10px; top: 11px; width: 340px; text-align: center;
    white-space: nowrap;
    font-family: "Bebas Neue", sans-serif; font-size: 58px; line-height: 58px;
    color: var(--black); letter-spacing: 0.5px;
  }
  .license {
    position: absolute; left: 81px; top: 65px; width: 199px; height: 37px;
    background: var(--black); color: var(--green);
    font-family: "Montserrat", sans-serif; font-weight: 500; font-size: 23px;
    line-height: 37px; text-align: center; white-space: nowrap;
  }
  .divider {
    position: absolute; left: 345px; top: 22px; width: 3px; height: 73px;
    background: var(--green-dark);
  }
  .contact-line {
    position: absolute; left: 369px; display: flex; align-items: center; gap: 9px;
    font-family: "Montserrat", sans-serif; font-weight: 500; font-size: 23px;
    color: var(--black); white-space: nowrap;
  }
  .contact-line--web { top: 13px; }
  .contact-line--mail { top: 54px; }
  .contact-line svg { width: 32px; height: 32px; flex: none; }
  .bottom-bar { position: absolute; left: 0; bottom: 0; width: 100%; height: 19px; background: var(--black); }
</style>
</head>
<body>
  <section class="sign">
    <svg class="sign__shapes" viewBox="0 0 937 469" aria-hidden="true">
      <polygon points="0,0 130,0 0,211" fill="var(--green)"/>
      <polygon points="150,0 196,0 113,137 67,137" fill="var(--white)"/>
      <polygon points="214,0 232,0 179,87 162,87" fill="var(--green)"/>
      <polygon points="807,0 937,0 937,211" fill="var(--green)"/>
      <polygon points="741,0 787,0 871,137 825,137" fill="var(--white)"/>
      <polygon points="706,0 723,0 799,87 783,87" fill="var(--green)"/>
    </svg>

    <div class="est est--left">ESTD</div>
    <div class="logo-mark" role="img" aria-label="Company logo mark"></div>
    <div class="est est--right">2020</div>

    <div class="brand">
      <span class="brand__name">THORNWELL</span>
      <span class="brand__tag">BUILDING COMPANY</span>
    </div>

    <h1 class="headline">BUILD WITH THE T-CREW!</h1>

    <div class="contact-band">
      <div class="phone">472-318-6095</div>
      <div class="license">Lic#5386204</div>
      <div class="divider"></div>

      <div class="contact-line contact-line--web">
        <svg viewBox="0 0 32 32" aria-hidden="true">
          <circle cx="16" cy="16" r="14" fill="none" stroke="var(--black)" stroke-width="2.5"/>
          <circle cx="16" cy="16" r="8" fill="none" stroke="var(--black)" stroke-width="1.8"/>
          <ellipse cx="16" cy="16" rx="3.5" ry="8" fill="none" stroke="var(--black)" stroke-width="1.5"/>
          <line x1="8" y1="16" x2="24" y2="16" stroke="var(--black)" stroke-width="1.5"/>
          <line x1="9.5" y1="12" x2="22.5" y2="12" stroke="var(--black)" stroke-width="1.2"/>
          <line x1="9.5" y1="20" x2="22.5" y2="20" stroke="var(--black)" stroke-width="1.2"/>
        </svg>
        <span>www.thornwellbuildingcompany.com</span>
      </div>

      <div class="contact-line contact-line--mail">
        <svg viewBox="0 0 32 32" aria-hidden="true">
          <circle cx="16" cy="16" r="14" fill="none" stroke="var(--black)" stroke-width="2.5"/>
          <rect x="8.5" y="11" width="15" height="10" fill="none" stroke="var(--black)" stroke-width="1.6"/>
          <polyline points="8.5,11 16,17 23.5,11" fill="none" stroke="var(--black)" stroke-width="1.6"/>
        </svg>
        <span>thornwellbuildingcompany@mailvistra.net</span>
      </div>
    </div>

    <div class="bottom-bar"></div>
  </section>
</body>
</html>
```